TCW Website

We need a website for a company based in Doha Qatar called Talent Crest Worldwide. It is a global recruitment company, that specializes in both mass recruitment and headhunting. The company is the number 1 one stop shop for recruitment in Qatar. It recruits from all over the world Europe, Asia, Americas, Middle East, Africa for Qatar.
Updates

Target Market(s)

Multinational companies, fortune 500 company CEO's, any top earning companies that are looking for a large number of employees or headhunting employees.
Also for candidates looking for companies to work in Qatar.

Industry/Entity Type

Shop

Colors
ffffff

Requirements
Must have
• Most important qualities the website needs to have:
Clean
Modern
Elegant
Professional
Less Tabs
Minimalisitc

Some examples, I would like you to follow are here:
http://www.velbrook.ca/
http://www.tornellaquin.com/
https://plivatrend.com/match#

The main color should be white and it has to have a very stylish, modern and cool look. While being minimalistic. I do not want too many tabs. I want it to be simplistic to understand. the only place where the pink logo color is should be in the logo. The logo color should not be anywhere else. It has to be absolutely sleek. Please follow the example websites that I have provided.

I will send the contact details you need to add later. There is no need for a log in page.

Whatever you think that may be important for a recruitment site do suggest. But there is no need for a log in area as we are a different kind of recruitment company.

There should be an area for testimonials from clients. There should also be an area for news flash for the latest countries we are hiring from and the latest companies we are hiring for and the latest positions we are looking for.

Show me the best please. Whoever gives me the best, I will give them an order for the 2nd website too.

Nice to have
• I have included a powerpoint to explain more!

```html
<!DOCTYPE html>
<html lang="en">
<head>
<meta charset="utf-8">
<title>Talent Crest Worldwide</title>
<link href="https://fonts.googleapis.com/css2?family=Roboto+Slab:wght@300;400;500;700&display=swap" rel="stylesheet">
<style>
  :root {
    --white: #ffffff;
    --ink: #111111;
    --brand: #a8235e;
    --sky-top: #241f38;
    --sky-mid: #352b4d;
    --sky-low: #3e2f48;
    --lights: #5a4232;
    --water: #15151f;
    --ticker-bg: #262626;
  }
  * { margin: 0; padding: 0; box-sizing: border-box; }
  html, body { width: 1200px; height: 900px; overflow: hidden; }
  body { font-family: "Roboto Slab", serif; background: var(--white); position: relative; }

  .site-header { position: absolute; left: 0; top: 0; width: 1200px; height: 128px; background: var(--white); border-top: 1px dashed #ddd; }
  .brand { position: absolute; left: 117px; top: 38px; display: flex; align-items: center; gap: 10px; }
  .brand-dot { width: 30px; height: 30px; border-radius: 50%; background: var(--brand); }
  .brand-name { color: var(--brand); font-weight: 700; font-size: 21px; line-height: 26px; width: 200px; }

  .social-link { position: absolute; left: 560px; top: 34px; width: 100px; text-align: right; font-size: 15px; font-weight: 400; color: var(--ink); text-decoration: none; }
  .signup-email { position: absolute; left: 677px; top: 27px; width: 255px; height: 35px; border: 1px dashed var(--ink); border-radius: 18px; font-size: 18px; font-weight: 300; padding-left: 20px; line-height: 33px; color: #333; white-space: nowrap; }
  .signup-button { position: absolute; left: 944px; top: 27px; width: 120px; height: 35px; background: var(--ink); color: var(--white); border-radius: 12px; font-size: 23px; text-align: center; line-height: 35px; white-space: nowrap; }

  .main-nav { position: absolute; top: 90px; left: 0; width: 1200px; }
  .main-nav a { position: absolute; font-size: 18px; font-weight: 500; color: var(--ink); text-decoration: none; white-space: nowrap; }
  .main-nav .is-active::after { content: ""; position: absolute; left: -1px; right: -1px; top: 31px; height: 6px; background: var(--ink); }

  .hero { position: absolute; left: 0; top: 128px; width: 1200px; height: 772px;
    background: linear-gradient(180deg, var(--sky-top) 0%, var(--sky-mid) 45%, var(--sky-low) 75%, var(--lights) 86%, var(--water) 92%, var(--water) 100%); }

  .ticker-hanger { position: absolute; top: 128px; width: 12px; height: 58px; background: var(--ink); }
  .ticker { position: absolute; left: 115px; top: 184px; width: 951px; height: 65px; background: var(--ticker-bg); border: 3px solid #000; color: var(--white); font-size: 34px; font-weight: 400; line-height: 59px; padding-left: 15px; white-space: nowrap; overflow: hidden; }
  .ticker-more { position: absolute; left: 487px; top: 244px; width: 198px; height: 40px; background: var(--ink); color: var(--white); border-radius: 0 0 16px 16px; font-size: 18px; font-weight: 300; text-align: center; line-height: 38px; white-space: nowrap; }

  .hero-title { position: absolute; left: 0; top: 410px; width: 1200px; text-align: center; color: var(--white); font-weight: 700; font-size: 68px; line-height: 86px; }
  .hero-cta { position: absolute; left: 441px; top: 700px; width: 301px; height: 64px; background: var(--ink); color: var(--white); border-radius: 16px; font-size: 30px; font-weight: 400; text-align: center; line-height: 64px; text-decoration: none; white-space: nowrap; }
</style>
</head>
<body>
  <header class="site-header">
    <div class="brand"><span class="brand-dot"></span><span class="brand-name">Talent Crest Worldwide</span></div>
    <a class="social-link" href="#">Friendloop</a>
    <div class="signup-email">enter your e-mail address</div>
    <div class="signup-button">SIGN UP</div>
    <nav class="main-nav">
      <a class="is-active" href="#" style="left:516px">Home</a>
      <a href="#" style="left:630px">Latest news</a>
      <a href="#" style="left:781px">Clients</a>
      <a href="#" style="left:896px">About</a>
      <a href="#" style="left:994px">Contact</a>
    </nav>
  </header>

  <section class="hero" role="img" aria-label="Night skyline of Doha towers lit up above the bay"></section>

  <div class="ticker-hanger" style="left:188px"></div>
  <div class="ticker-hanger" style="left:978px"></div>
  <div class="ticker">TCW is now coming to Nepal to recruit for Dunecrest Qatar</div>
  <div class="ticker-more">click for more news</div>

  <h1 class="hero-title">Qatar’s leading<br>One-Stop-Shop for Global<br>Recruitment!</h1>
  <a class="hero-cta" href="#">BROWSE CLIENTS</a>
</body>
</html>
```